Business cards Marta Kessel Sport & Events

I need new business cards to match my new logo design for my company called "Marta Kessel Sport & Events". I'm based in Germany.
With my company, I offer different services in the context of sport.

Marta Kessel owner

Marta Kessel Sports & Events
Birkenfelder Weg 12
D-63118 Offenbach

+49 69 / 31 52 94 07
info@marta-kessel.example
www.marta-kessel.example

Contact Information for Business Card

Marta Kessel Inhaberin Marta Kessel Sport & Events Birkenfelder Weg 12 D-63118 Offenbach +49 69 / 31 52 94 07 info@marta-kessel.example www.marta-kessel.example

Requirements
Must have
• Logo | Double sided business card

```html
<!DOCTYPE html>
<html lang="de">
<head>
<meta charset="utf-8">
<title>Marta Kessel Sport &amp; Events – Visitenkarte</title>
<link rel="stylesheet" href="https://fonts.googleapis.com/css2?family=Montserrat:wght@400;500;700&display=swap">
<style>
  :root {
    --bg: #4a5056;
    --ink: #1b1b1d;
    --paper: #ffffff;
    --accent: #f7a21b;
    --muted: #2a2a2c;
  }
  * { box-sizing: border-box; margin: 0; padding: 0; }
  html, body { width: 1200px; height: 900px; overflow: hidden; }
  body {
    background: var(--bg);
    font-family: "Montserrat", sans-serif;
    display: flex;
    align-items: center;
    justify-content: center;
    gap: 40px;
  }
  .card {
    position: relative;
    width: 540px;
    height: 340px;
    border-radius: 18px;
    overflow: hidden;
  }
  /* back side */
  .card--back {
    background: var(--ink);
    display: flex;
    align-items: center;
    justify-content: center;
    gap: 26px;
  }
  .brand-dot {
    width: 96px; height: 96px;
    border-radius: 50%;
    background: var(--accent);
    flex: none;
  }
  .brand-name {
    color: var(--paper);
    font-weight: 700;
    text-transform: uppercase;
    line-height: 1.15;
  }
  .brand-name__main { display: block; font-size: 34px; letter-spacing: 2px; }
  .brand-name__sub { display: block; font-size: 15px; letter-spacing: 6px; margin-top: 4px; }

  /* front side */
  .card--front { background: var(--paper); }
  .front-shapes { position: absolute; inset: 0; }
  .front-wordmark {
    position: absolute; left: 34px; top: 42px;
    color: var(--ink);
    font-weight: 700;
    text-transform: uppercase;
    line-height: 1.15;
  }
  .front-wordmark .brand-name__main { font-size: 24px; letter-spacing: 1.5px; }
  .front-wordmark .brand-name__sub { font-size: 11px; letter-spacing: 5px; margin-top: 2px; }
  .owner {
    position: absolute; right: 44px; top: 30px;
    text-align: right;
  }
  .owner__name { color: var(--accent); font-size: 17px; font-weight: 500; text-transform: uppercase; }
  .owner__role { color: var(--ink); font-size: 13px; }
  .address {
    position: absolute; left: 34px; top: 138px;
    font-size: 13px; line-height: 1.45; color: var(--ink);
  }
  .address__company { color: var(--accent); }
  .contact {
    position: absolute; left: 38px; top: 244px;
    list-style: none;
    color: var(--paper);
    font-size: 12.5px;
    line-height: 1.6;
  }
  .contact li { display: flex; align-items: center; gap: 10px; }
  .contact svg { width: 12px; height: 12px; flex: none; }
</style>
</head>
<body>

  <section class="card card--back" aria-label="Rückseite">
    <span class="brand-dot" aria-hidden="true"></span>
    <p class="brand-name">
      <span class="brand-name__main">Marta Kessel</span>
      <span class="brand-name__sub">Sport &amp; Events</span>
    </p>
  </section>

  <section class="card card--front" aria-label="Vorderseite">
    <svg class="front-shapes" viewBox="0 0 540 340" aria-hidden="true">
      <rect x="510" y="20" width="30" height="40" fill="var(--accent)"/>
      <rect x="420" y="188" width="120" height="66" fill="var(--accent)"/>
      <rect x="0" y="240" width="410" height="82" fill="var(--ink)"/>
      <circle cx="415" cy="238" r="54" fill="var(--paper)"/>
      <circle cx="415" cy="238" r="46" fill="var(--accent)"/>
    </svg>

    <p class="front-wordmark">
      <span class="brand-name__main">Marta Kessel</span>
      <span class="brand-name__sub">Sport &amp; Events</span>
    </p>

    <div class="owner">
      <p class="owner__name">Marta Kessel</p>
      <p class="owner__role">owner</p>
    </div>

    <address class="address" style="font-style:normal">
      <span class="address__company">Marta Kessel Sports &amp; Events</span><br>
      Birkenfelder Weg 12<br>
      D-63118 Offenbach
    </address>

    <ul class="contact">
      <li>
        <svg viewBox="0 0 24 24"><path fill="var(--accent)" d="M6.6 10.8a15 15 0 0 0 6.6 6.6l2.2-2.2c.3-.3.7-.4 1-.2 1.1.4 2.3.6 3.6.6.6 0 1 .4 1 1V20c0 .6-.4 1-1 1A17 17 0 0 1 3 4c0-.6.4-1 1-1h3.5c.6 0 1 .4 1 1 0 1.3.2 2.5.6 3.6.1.3 0 .7-.2 1z"/></svg>
        +49 69 / 31 52 94 07
      </li>
      <li>
        <svg viewBox="0 0 24 24"><rect x="2.5" y="5" width="19" height="14" rx="1.5" fill="none" stroke="var(--accent)" stroke-width="2.5"/><path d="M3 6l9 7 9-7" fill="none" stroke="var(--accent)" stroke-width="2.5"/></svg>
        info@marta-kessel.example
      </li>
      <li>
        <svg viewBox="0 0 24 24"><circle cx="12" cy="12" r="9.5" fill="none" stroke="var(--accent)" stroke-width="2.5"/><path d="M2.5 12h19M12 2.5c3 3 3 16 0 19M12 2.5c-3 3-3 16 0 19" fill="none" stroke="var(--accent)" stroke-width="2"/></svg>
        www.marta-kessel.example
      </li>
    </ul>
  </section>

</body>
</html>
```